Tilda Tinkerwire, An IT Company Has New Logo, Need Fresh Business Cards

IT company is called Tilda Tinkerwire and is displayed nicely with the new logo from here on pitchloft. Would like a fresh business card look that encompasses the idea that we want clients to Cherish Every Gadget. I love the use of circuitry with hearts as endpoints and x's and o's. It needs to have room for my certification logos of which there are 4 and a BRJ Alumni log. I am attaching my current card to illustrate how it has always captured attention, but that was in the early stages of business when I was doing more residential work. I am focused on businesses now, so a level of professionalism is necessary. I would also like the card to lend itself well to additional stationary, email signature, ticketing template for my workboard, etc. For the time being, I need the card for an upcoming conference so that work will come later. Color scheme should be that of the new logo. Thank you and I look forward to the designs.

Target Market(s)

Businesses looking for IT services.

Industry/Entity Type

Information Technology

Contact Information for Business Card

See above

Requirements
Must have
• New logo colors and a warm feel. Possibly a tad feminine as I am female, but appealing to males.
Nice to have
• I would like techy, but no too much so. I like friendly and connecting feels. People LOVED my old card and called me because it gave them a warm feeling.

```html
<!DOCTYPE html>
<html lang="en">
<head>
<meta charset="utf-8">
<title>Tilda Tinkerwire — Business Cards</title>
<link rel="stylesheet" href="https://fonts.googleapis.com/css2?family=Quicksand:wght@500;600&family=Exo+2:wght@700&family=Open+Sans:wght@400;600&display=swap">
<style>
  :root {
    --stage-light: #7a7a7a;
    --stage-dark: #3a3a3a;
    --card-dark: #2b2b2b;
    --card-light: #ffffff;
    --sky: #7cc6e6;
    --lime: #c3de6e;
    --rose: #ef9cc8;
    --ink: #4a4a4a;
    --ink-soft: #6a6a6a;
    --paper-text: #f2f2f2;
  }
  * { box-sizing: border-box; margin: 0; padding: 0; }
  html, body { width: 1200px; height: 1000px; overflow: hidden; }
  body {
    position: relative;
    background: radial-gradient(ellipse at 50% 35%, var(--stage-light), var(--stage-dark) 80%);
    font-family: "Open Sans", sans-serif;
  }
  .card {
    position: absolute;
    width: 560px;
    height: 320px;
    border-radius: 26px;
    overflow: hidden;
    box-shadow: 0 18px 30px rgba(0,0,0,0.35);
  }
  /* Back */
  .card-back { left: 90px; top: 130px; background: var(--card-dark); }
  .card-back .texture { position: absolute; inset: 0; background: radial-gradient(circle at 50% 45%, #333 0%, var(--card-dark) 70%); }
  .brand-block { position: absolute; left: 0; right: 0; top: 92px; text-align: center; }
  .brand-dot { display: inline-block; width: 54px; height: 54px; border-radius: 50%; border: 3px solid var(--rose); margin-bottom: 16px; }
  .brand-name { font-family: "Quicksand", sans-serif; font-weight: 600; color: var(--sky); line-height: 1; }
  .card-back .brand-name { font-size: 30px; }
  .tagline { font-family: "Quicksand", sans-serif; font-weight: 600; color: var(--rose); text-transform: uppercase; letter-spacing: 3px; }
  .card-back .tagline { font-size: 9.5px; margin-top: 4px; }
  .back-url { position: absolute; left: 0; right: 0; bottom: 46px; text-align: center; color: var(--paper-text); font-size: 12px; letter-spacing: 2.5px; }
  .back-url span { color: var(--sky); }

  /* Front */
  .card-front { left: 550px; top: 530px; background: var(--card-light); }
  .front-wordmark { position: absolute; left: 36px; top: 40px; }
  .front-wordmark .brand-name { font-size: 40px; }
  .front-wordmark .tagline { font-size: 11px; margin-top: 4px; }
  .holder { position: absolute; left: 56px; top: 128px; }
  .holder-name { font-family: "Exo 2", sans-serif; font-weight: 700; font-size: 22px; letter-spacing: 1px; color: var(--sky); }
  .holder-name .last { color: var(--lime); }
  .holder-role { font-size: 14px; color: var(--ink-soft); margin-top: 2px; }
  .side-tab { position: absolute; left: 0; top: 128px; width: 8px; height: 34px; background: var(--sky); border-radius: 0 6px 6px 0; }
  .address { position: absolute; left: 56px; top: 190px; font-size: 12.5px; color: var(--ink); line-height: 1.4; }
  .contacts { position: absolute; left: 36px; top: 238px; list-style: none; font-size: 12.5px; color: var(--ink); }
  .contacts li { display: flex; align-items: center; gap: 10px; height: 18px; }
  .contacts svg { width: 10px; height: 10px; fill: var(--sky); }
  .contacts .hl { color: var(--sky); }
  .front-logo { position: absolute; right: 36px; top: 78px; width: 190px; text-align: center; }
  .front-logo .brand-dot { width: 46px; height: 46px; margin-bottom: 12px; }
  .front-logo .brand-name { font-size: 22px; }
  .front-logo .tagline { font-size: 7px; letter-spacing: 2px; margin-top: 3px; }
  .colour-band { position: absolute; left: 0; bottom: 0; width: 100%; height: 12px; display: flex; }
  .colour-band .sky { flex: 34; background: var(--sky); }
  .colour-band .lime { flex: 34; background: var(--lime); }
  .colour-band .rose { flex: 32; background: var(--rose); }
</style>
</head>
<body>
  <section class="card card-back">
    <div class="texture" role="img" aria-label="Subtle repeating ring pattern on dark card surface"></div>
    <div class="brand-block">
      <span class="brand-dot"></span>
      <div class="brand-name">Tilda Tinkerwire</div>
      <div class="tagline">Cherish Every Gadget</div>
    </div>
    <p class="back-url">www.<span>websitename</span>.com</p>
  </section>

  <section class="card card-front">
    <div class="front-wordmark">
      <div class="brand-name">Tilda Tinkerwire</div>
      <div class="tagline">Cherish Every Gadget</div>
    </div>
    <span class="side-tab"></span>
    <div class="holder">
      <h1 class="holder-name">NORA <span class="last">VELLACOTT</span></h1>
      <p class="holder-role">Founder/CEO</p>
    </div>
    <p class="address">Your Street Address<br>Singapore, 1234</p>
    <ul class="contacts">
      <li><svg viewBox="0 0 10 10"><path d="M2 0.5 L3.8 2.6 L2.9 3.6 Q4 6 6.4 7.1 L7.4 6.2 L9.5 8 L8.3 9.5 Q3.5 9 0.5 1.7 Z"/></svg>+000 123 456 789</li>
      <li><svg viewBox="0 0 10 10"><path d="M0 2 H10 V8.5 H0 Z M0 2 L5 5.6 L10 2" stroke="#fff" stroke-width="0.8"/></svg>urname@email.com</li>
      <li><svg viewBox="0 0 10 10"><circle cx="5.5" cy="4.5" r="3.6" fill="none" stroke="#7cc6e6" stroke-width="1.4"/><path d="M1 9.5 L3 6.5 L4 7.5 Z"/></svg>www.<span class="hl">websitename</span>.com</li>
    </ul>
    <div class="front-logo">
      <span class="brand-dot"></span>
      <div class="brand-name">Tilda Tinkerwire</div>
      <div class="tagline">Cherish Every Gadget</div>
    </div>
    <div class="colour-band"><span class="sky"></span><span class="lime"></span><span class="rose"></span></div>
  </section>
</body>
</html>
```